Colocation Data Center Web Site

Would be to design a specialized site specifically for a Data Center that provide colocation services to their clients.
This site would need to have a client portal to allow them to see the status of their bills, list of services and to create service tickets.

Industry/Entity Type

It Service

```html
<!DOCTYPE html>
<html lang="en">
<head>
<meta charset="utf-8">
<title>Norvale Colocation Data Centre</title>
<link href="https://fonts.googleapis.com/css2?family=Bebas+Neue&family=Roboto:wght@400;500&family=Raleway:wght@300;400&display=swap" rel="stylesheet">
<style>
:root{
  --green:#78a60f;
  --heading:#6e9c10;
  --dark:#2b2b2b;
  --footer:#333333;
  --text:#8a8a8a;
  --line:#dcdcdc;
  --white:#ffffff;
}
*{box-sizing:border-box;margin:0;padding:0}
html,body{width:800px;height:1200px;overflow:hidden;background:var(--white)}
body{position:relative;font-family:"Raleway",sans-serif;color:var(--text)}
.abs{position:absolute}
.topbar{left:0;top:0;width:800px;height:65px;background:var(--green)}
.brand{left:83px;top:14px;font-family:"Bebas Neue",sans-serif;font-size:27px;color:var(--white);letter-spacing:.5px}
.login{left:633px;top:19px;width:84px;height:23px;background:var(--white);border-radius:2px;font-family:"Roboto",sans-serif;font-size:10px;color:#333;display:flex;align-items:center}
.login span{padding-left:7px;flex:1}
.login i{width:18px;height:100%;border-left:1px solid #ccc;display:flex;align-items:center;justify-content:center}
.nav{left:83px;top:46px;width:634px;height:34px;background:var(--dark);z-index:2;display:flex;align-items:center;padding-left:20px;border-radius:2px}
.nav a{font-family:"Roboto",sans-serif;font-size:10.5px;color:var(--white);text-decoration:none;margin-right:22px}
.search{position:absolute;right:7px;top:8px;width:142px;height:18px;background:var(--white);border-radius:2px;font-size:6px;color:#bbb;padding:5px 6px}
.hero{left:0;top:65px;width:800px;height:283px;background:linear-gradient(180deg,#e4e6e8 0%,#bfc3c6 45%,#8e9396 70%,#e9eaeb 100%)}
.dots{left:379px;top:325px;display:flex;gap:3px}
.dots b{width:9px;height:9px;border-radius:50%;background:#e6e6e6;border:1px solid #999}
.dots b:first-child{background:#444}
.news{left:0;top:348px;width:800px;height:51px;background:var(--dark)}
.news h2{position:absolute;left:83px;top:12px;font-family:"Bebas Neue",sans-serif;font-weight:400;font-size:26px;color:var(--white)}
.news p{position:absolute;left:200px;top:20px;font-size:9.5px;color:#ddd}
.arrows{position:absolute;left:685px;top:20px;display:flex;gap:3px}
h3{position:absolute;font-family:"Roboto",sans-serif;font-weight:500;font-size:12px;color:var(--heading)}
.rule{position:absolute;height:1px;background:var(--line)}
.ph{position:absolute}
.copy{position:absolute;font-size:8.6px;line-height:16px;font-weight:300;text-align:justify}
.btn{position:absolute;top:797px;width:74px;height:26px;background:var(--green);color:var(--white);font-family:"Roboto",sans-serif;font-size:10px;display:flex;align-items:center;justify-content:center}
.clients{left:513px;top:900px;width:206px;display:grid;grid-template-columns:repeat(3,1fr);row-gap:18px;font-family:"Roboto",sans-serif;font-weight:500;font-size:11px;color:#2d5f8a;text-align:center}
.clients .wide{grid-column:span 2}
.footer{left:0;top:992px;width:800px;height:208px;background:var(--footer)}
.footer h4{position:absolute;top:27px;font-family:"Roboto",sans-serif;font-weight:400;font-size:8.5px;color:var(--green)}
.footer ul{position:absolute;top:50px;list-style:none;font-size:9.5px;line-height:16px;color:#e0e0e0}
.signup{position:absolute;left:405px;top:45px;width:147px;font-size:9.5px;line-height:13px;color:#e0e0e0;text-align:justify}
.field{position:absolute;left:405px;width:147px;height:18px;background:#fff;border:1px solid #ccc;font-size:7px;color:#ccc;padding:4px 8px}
.sub{position:absolute;left:487px;top:135px;width:65px;height:16px;border-radius:8px;background:var(--green);color:#fff;font-size:8px;display:flex;align-items:center;justify-content:center}
.social{position:absolute;left:617px;width:100px;display:flex;align-items:center;justify-content:space-between;font-size:9.5px;color:#e0e0e0}
.social i{width:18px;height:18px;border-radius:50%;background:#fff}
.legal{position:absolute;left:0;width:800px;top:166px;text-align:center;font-size:9.5px;color:#e0e0e0}
</style>
</head>
<body>
<div class="abs topbar"></div>
<div class="abs brand">NORVALE</div>
<div class="abs login"><span>USER LOGIN</span><i><svg width="8" height="6"><path d="M0 0h8L4 6z" fill="#333"/></svg></i></div>
<nav class="abs nav">
  <a>Home</a><a>Aboout Us</a><a>Services</a><a>Equipment</a><a>Resources</a><a>Support</a><a>Contact Us</a>
  <div class="search">Type search</div>
</nav>
<div class="abs hero" role="img" aria-label="Rows of server racks in a bright data centre hall"></div>
<div class="abs dots"><b></b><b></b><b></b><b></b></div>

<section class="abs news">
  <h2>LATEST NEWS</h2>
  <p>Lorem Ipsum has been the industry's standard dummy text ever since the 1500s, when an unknown &nbsp;&nbsp;&nbsp;...</p>
  <div class="arrows">
    <svg width="14" height="14"><circle cx="7" cy="7" r="7" fill="#ccc"/><path d="M8.5 4 5.5 7l3 3" stroke="#333" stroke-width="1.6" fill="none"/></svg>
    <svg width="14" height="14"><circle cx="7" cy="7" r="7" fill="#ccc"/><path d="M5.5 4l3 3-3 3" stroke="#333" stroke-width="1.6" fill="none"/></svg>
  </div>
</section>

<h3 style="left:83px;top:424px">WELCOME TO COLOCATION DATA CENTRE</h3>
<div class="ph" style="left:83px;top:451px;width:207px;height:101px;background:linear-gradient(90deg,#5e7fa6,#9fb5cc 60%,#eef1f4)" role="img" aria-label="Technician working with a laptop beside server racks"></div>
<p class="copy" style="left:298px;top:452px;width:420px">Lorem Ipsum is simply dummy text of the printing and typesetting industry. Lorem Ipsum has been the industry's standard dummy text ever since the 1500s, when an unknown printer took a galley of type and scrambled it to make a type specimen book. It has survived not only five centuries, but also the leap into electronic typesetting, remaining essentially unchanged.<br>It was popularised in the 1960s with the release of Lettrova sheets containing Lorem Ipsum passages, and more recently with desktop publishing software like Quillset Pagecraft including versions of Lorem Ipsum.</p>

<h3 style="left:83px;top:572px">SECURITY</h3>
<h3 style="left:297px;top:572px">FLEXIBILITY</h3>
<h3 style="left:510px;top:572px">TECHNICAL SUPPORT</h3>
<div class="rule" style="left:83px;top:589px;width:207px"></div>
<div class="rule" style="left:297px;top:589px;width:206px"></div>
<div class="rule" style="left:510px;top:589px;width:207px"></div>
<div class="ph" style="left:83px;top:598px;width:207px;height:102px;background:radial-gradient(circle at 50% 45%,#3f8fc4,#0d2a4a 70%)" role="img" aria-label="Glowing padlock over a digital security background"></div>
<div class="ph" style="left:297px;top:598px;width:206px;height:102px;background:linear-gradient(90deg,#2c2f33,#5b6a70 55%,#9dbfc3)" role="img" aria-label="Businessman holding a tablet computer"></div>
<div class="ph" style="left:510px;top:598px;width:207px;height:102px;background:linear-gradient(90deg,#f2f2f2,#c9b9aa 60%,#8a6e5a)" role="img" aria-label="Support staff wearing headsets"></div>
<p class="copy" style="left:85px;top:706px;width:201px">Lorem Ipsum is simply dummy text of the printing and typesetting industry. Lorem Ipsum has been the industry's standard dummy text ever since the 1500s, when an unknown printer took a galley of type and scrambled Ipsum.</p>
<p class="copy" style="left:298px;top:706px;width:201px">Lorem Ipsum is simply dummy text of the printing and typesetting industry. Lorem Ipsum has been the industry's standard dummy text ever since the 1500s, when an unknown printer took a galley of type and scrambled Ipsum.</p>
<p class="copy" style="left:512px;top:706px;width:202px">Lorem Ipsum is simply dummy text of the printing and typesetting industry. Lorem Ipsum has been the industry's standard dummy text ever since the 1500s, when an unknown printer took a galley of type and scrambled Ipsum.</p>
<div class="btn" style="left:85px">READ MORE</div>
<div class="btn" style="left:296px">READ MORE</div>
<div class="btn" style="left:510px">READ MORE</div>

<h3 style="left:83px;top:858px">TESTIMONIALS</h3>
<h3 style="left:513px;top:858px">CLIENTS</h3>
<div class="rule" style="left:83px;top:876px;width:420px"></div>
<div class="rule" style="left:513px;top:876px;width:204px"></div>
<div class="ph" style="left:91px;top:898px;width:84px;height:63px;background:linear-gradient(160deg,#e0e0e0,#c98e6b 55%,#d8402c)" role="img" aria-label="Portrait of a client"></div>
<svg class="ph" style="left:194px;top:898px" width="15" height="11"><text x="0" y="14" font-size="22" font-family="Georgia,serif" fill="#555">“</text></svg>
<p class="copy" style="left:216px;top:899px;width:283px">Lorem Ipsum is simply dummy text of the printing and typesetting industry. Lorem Ipsum has been the industry's standard dummy text ever since the 1500s, when an unknown printer took a galley of type and scrambled Ipsum. <b style="color:#444;font-family:Georgia,serif">”</b> <span style="color:var(--green);font-weight:400">By Daniel Harlow</span></p>
<div class="abs clients"><span>Corelink</span><span>Stratum</span><span>Hexrack</span><span class="wide">Nordgrid</span><span>Baystack</span></div>

<footer class="abs footer">
  <h4 style="left:83px">QUICK LINKS</h4>
  <h4 style="left:244px">SUPPORT LINKS</h4>
  <h4 style="left:405px">NEWSLETTER SIGNUP</h4>
  <h4 style="left:617px">CONNECT WITH US</h4>
  <ul style="left:83px"><li>Home</li><li>About Us</li><li>Services</li><li>Service Plans</li><li>News</li><li>FAQ &amp; Wiki</li><li>Contact Us</li></ul>
  <ul style="left:244px;width:80px"><li>Legal Notice</li><li>Privacy Policy</li><li>Terms &amp; Condi-<br>tions</li><li>Help</li></ul>
  <p class="signup">Sign-up for our daily emails by entering your information</p>
  <div class="field" style="top:81px">Name</div>
  <div class="field" style="top:109px">Enter Your E-Mail ID</div>
  <div class="sub">Subscribe</div>
  <div class="social" style="top:46px"><i></i><span>Chirper</span></div>
  <div class="social" style="top:72px"><i></i><span>Friendbook</span></div>
  <div class="social" style="top:97px"><i></i><span>Workline</span></div>
  <p class="legal">Copyright ©2013 Company Name &nbsp;- All rights reserved</p>
</footer>
</body>
</html>
```